Cardiology Practice needs a Heart Scan Order Form

Busy cardiology practice needs an order form for a heart scan test. Sample is attached. One side should have all information noted and the other side should have our physician names (Vikram Joshi, MD, K.L. Morvandi, MD, Anjali Desai, MD, Parvin Joshi, MD, and Gerald Montefino, MD. It should have the map that is uploaded and our demographic information (Crestline Cardio PLLC, 218 Juniper Ave. Ste. B, Webster, TX 77412 along with phone 713-642-1187 and fax 713-642-1188) as well as our web address (crestlinecardio.example). Our primary colors are red, black and white. Needs to fit paper size 8 1/2 by 11.

Target Market(s)

Healthcare

Industry/Entity Type

Health Care

Font styles to use
Serif

Colors
ec1f27

Requirements
Must have
• Logo, information listed on sample form, demographics and physician names as well as website.
Nice to have
• Open to suggestions
Should not have
• Physician Pictures

```html
<!DOCTYPE html>
<html lang="en">
<head>
<meta charset="utf-8">
<title>Crestline Cardio – Calcium Score Heart Scan Order Form</title>
<link href="https://fonts.googleapis.com/css2?family=Montserrat:wght@500;600;700;800&family=Roboto:ital,wght@0,300;0,400;0,500;0,700;1,400;1,500&display=swap" rel="stylesheet">
<style>
:root{
  --red:#c0323b;
  --brand-red:#ec1f27;
  --ink:#2b2b2b;
  --black:#0c0c0c;
  --paper:#f7f7f7;
  --stage:#e8e8e8;
  --field:#e4e4e4;
  --rule:#8a8a8a;
  --map:#e3e3e0;
}
*{box-sizing:border-box;margin:0;padding:0}
html,body{width:1200px;height:782px;overflow:hidden;background:var(--stage)}
body{position:relative;font-family:'Roboto',Arial,sans-serif;color:var(--ink)}
.page{position:absolute;top:80px;width:479px;height:621px;background:var(--paper);overflow:hidden}
.page--front{left:104px}
.page--form{left:627px}
.abs{position:absolute}

/* brand */
.brand{display:flex;align-items:center;gap:7px;font-family:'Montserrat',sans-serif;font-weight:800;color:var(--red);text-transform:uppercase;letter-spacing:.5px}
.brand__dot{border-radius:50%;background:var(--red)}
.page--front .brand{left:0;right:0;top:54px;justify-content:center;font-size:27px}
.page--front .brand__dot{width:20px;height:20px}
.page--form .brand{left:21px;top:56px;font-size:21px}
.page--form .brand__dot{width:16px;height:16px}

/* physician band */
.physicians{left:0;top:122px;width:479px;height:103px;
  background:repeating-linear-gradient(135deg,#efefef 0 2px,#f8f8f8 2px 5px)}
.pill{position:absolute;height:23px;border-radius:12px;display:flex;align-items:center;justify-content:center;
  font-family:'Montserrat',sans-serif;font-weight:600;font-size:10.5px;color:#fff;background:var(--black)}
.pill--red{background:var(--red)}
.map{left:0;top:225px;width:479px;height:282px;background:linear-gradient(160deg,#ebebe8 0%,var(--map) 55%,#e9e6d2 100%)}
.footer-band{left:0;top:510px;width:479px;height:111px;background:var(--red);color:#fff;text-align:center;font-family:'Montserrat',sans-serif}
.footer-band__phones{margin-top:23px;font-size:11px;font-weight:500}
.footer-band__web{font-size:24px;font-weight:700;margin-top:2px;letter-spacing:-.2px}
.footer-band__addr{font-size:10.5px;font-weight:500;margin-top:3px}

/* form header */
.title{right:21px;top:36px;text-align:right;font-family:'Montserrat',sans-serif;line-height:1}
.title__top{color:var(--red);font-weight:500;font-size:20px}
.title__main{color:var(--ink);font-weight:800;font-size:25.5px;margin-top:2px}
.title__rule{height:3px;background:var(--red);margin-top:5px}

.schedule-tag{left:21px;top:117px;width:140px;height:16px}
.schedule-tag span{position:absolute;left:9px;top:0;font-family:'Montserrat',sans-serif;font-weight:800;font-size:12px;letter-spacing:.6px;color:var(--ink);line-height:16px}
.label{font-size:8.5px;color:var(--ink);white-space:nowrap}
.line{position:absolute;height:0;border-top:.7px solid var(--rule)}
.bar{height:14px;color:#fff;font-family:'Montserrat',sans-serif;font-weight:700;font-size:10.5px;letter-spacing:1.4px;display:flex;align-items:center;justify-content:center}
.bar--red{background:var(--red)}
.bar--dark{background:#333}
.check{position:absolute;width:8.5px;height:8.5px;border:.8px solid #444;background:#fff}
.opt{font-size:7.6px}
.sexbox{position:absolute;width:8px;height:8px;border:.7px solid #444;font-size:5.5px;line-height:7px;text-align:center}
.divider{left:21px;top:393px;width:437px;height:5px;background:repeating-linear-gradient(135deg,#bbb 0 1px,transparent 1px 3px)}
.notice{left:21px;top:406px;font-size:7.9px;font-style:italic;font-weight:500;white-space:nowrap}
.rules{font-size:6.1px;line-height:7.6px;color:#333}
.rules li{position:absolute;list-style:none;padding-left:10px}
.tick{position:absolute;left:0;top:0;width:7px;height:7px}
.ack{left:21px;top:508px;width:440px;font-size:6.9px;font-style:italic;font-weight:500;line-height:8.4px}
.sig{position:absolute;width:132px;height:31px;background:var(--field);border-radius:4px;overflow:hidden}
.sig__head{height:13px;padding-left:9px;font-size:7.3px;color:#fff;line-height:13px}
.sig__head--red{background:var(--red)}
.sig__head--dark{background:#333}
.referral{left:297px;top:533px;width:161px;height:67px;background:var(--field);border-radius:4px;overflow:hidden}
.referral__head{height:17px;background:#333;color:#fff;font-size:7.8px;line-height:17px;padding-left:12px}
.referral__row{height:16.6px;border-bottom:1px solid #f7f7f7;font-size:5.8px;line-height:16px;padding-left:11px;font-weight:500}
</style>
</head>
<body>

<section class="page page--front">
  <div class="abs brand"><span class="brand__dot"></span>Crestline Cardio</div>

  <div class="abs physicians">
    <div class="pill" style="left:25px;top:21px;width:133px">Vikram Joshi, MD</div>
    <div class="pill pill--red" style="left:170px;top:21px;width:134px">K.L. Morvandi, MD</div>
    <div class="pill" style="left:316px;top:21px;width:133px">Anjali Desai, MD</div>
    <div class="pill" style="left:-12px;top:58px;width:97px"></div>
    <div class="pill pill--red" style="left:100px;top:58px;width:134px">Parvin Joshi, MD</div>
    <div class="pill" style="left:246px;top:58px;width:134px">Gerald Montefino, MD</div>
    <div class="pill" style="left:393px;top:58px;width:100px"></div>
  </div>

  <div class="abs map" role="img" aria-label="Street map of Webster, TX showing the Crestline Cardio office location and nearby landmarks"></div>

  <div class="abs footer-band">
    <p class="footer-band__phones">Phone 713-642-1187 &nbsp;&nbsp;|&nbsp;&nbsp; Fax 713-642-1188</p>
    <p class="footer-band__web">www.crestlinecardio.example</p>
    <p class="footer-band__addr">Crestline Cardio PLLC, 218 Juniper Ave. Ste. B, Webster, TX 77412</p>
  </div>
</section>

<section class="page page--form">
  <div class="abs brand"><span class="brand__dot"></span>Crestline Cardio</div>

  <div class="abs title">
    <div class="title__top">CALCIUM SCORE</div>
    <div class="title__main">HEART SCAN</div>
    <div class="title__rule"></div>
  </div>

  <div class="abs schedule-tag">
    <svg width="140" height="16" viewBox="0 0 140 16"><path d="M0.5 0.5H128L139 8L128 15.5H0.5Z" fill="#fff" stroke="#555" stroke-width=".8"/></svg>
    <span>TEST SCHEDULE</span>
  </div>
  <span class="abs label" style="left:187px;top:121px">TEST DATE:</span>
  <div class="line" style="left:237px;top:131px;width:77px"></div>
  <span class="abs label" style="left:330px;top:122px">TEST TIME:</span>
  <div class="line" style="left:378px;top:131px;width:79px"></div>

  <div class="abs bar bar--red" style="left:21px;top:141px;width:219px">PATIENT INFORMATION</div>
  <div class="abs bar bar--dark" style="left:240px;top:141px;width:218px">CONTACT INFORMATION</div>

  <span class="abs label" style="left:21px;top:170px">Last Name</span>
  <span class="abs label" style="left:100px;top:170px">First Name</span>
  <span class="abs label" style="left:177px;top:170px">MI</span>
  <span class="abs label" style="left:250px;top:170px">Address</span>
  <div class="line" style="left:287px;top:177px;width:171px"></div>
  <div class="line" style="left:21px;top:196px;width:73px"></div>
  <div class="line" style="left:100px;top:196px;width:72px"></div>
  <div class="line" style="left:177px;top:196px;width:53px"></div>
  <div class="line" style="left:250px;top:196px;width:208px"></div>

  <span class="abs label" style="left:21px;top:209px">Date of Birth</span>
  <span class="abs label" style="left:129px;top:209px">Account No.</span>
  <span class="abs label" style="left:250px;top:209px">Home Phone No.</span>
  <span class="abs label" style="left:357px;top:209px">Mobile Phone No.</span>
  <div class="line" style="left:21px;top:234px;width:102px"></div>
  <div class="line" style="left:129px;top:234px;width:101px"></div>
  <div class="line" style="left:250px;top:234px;width:100px"></div>
  <div class="line" style="left:357px;top:234px;width:101px"></div>

  <div class="abs bar bar--red" style="left:21px;top:248px;width:437px">MEDICAL INFORMATION</div>

  <span class="abs label" style="left:21px;top:276px">Sex:</span>
  <span class="sexbox" style="left:43px;top:277px">F</span>
  <span class="sexbox" style="left:59px;top:277px">M</span>
  <span class="abs label" style="left:79px;top:276px">Height:</span>
  <div class="line" style="left:108px;top:284px;width:77px"></div>
  <span class="abs label" style="left:197px;top:276px">Weight</span>
  <div class="line" style="left:227px;top:284px;width:76px"></div>
  <span class="abs label" style="left:316px;top:276px">Race:</span>
  <div class="line" style="left:341px;top:284px;width:116px"></div>

  <span class="abs label" style="left:21px;top:298px">Diagnosis:</span>
  <div class="line" style="left:66px;top:306px;width:391px"></div>

  <span class="check" style="left:22px;top:321px"></span><span class="abs opt" style="left:36px;top:321px">PCI (no. of stents: <span style="display:inline-block;width:53px;border-bottom:.7px solid var(--rule)"></span> )</span>
  <span class="check" style="left:180px;top:321px"></span><span class="abs opt" style="left:193px;top:321px">CABG (no. of vessels: <span style="display:inline-block;width:45px;border-bottom:.7px solid var(--rule)"></span> )</span>
  <span class="check" style="left:341px;top:321px"></span><span class="abs opt" style="left:355px;top:321px">MI (last event: <span style="display:inline-block;width:45px;border-bottom:.7px solid var(--rule)"></span>)</span>

  <span class="check" style="left:22px;top:348px"></span><span class="abs opt" style="left:36px;top:348px">PCM/ICD</span>
  <span class="check" style="left:98px;top:348px"></span><span class="abs opt" style="left:112px;top:348px">Diabetes</span>
  <span class="check" style="left:172px;top:348px"></span><span class="abs opt" style="left:187px;top:348px">Claustrophobia</span>
  <span class="check" style="left:269px;top:348px"></span><span class="abs opt" style="left:284px;top:347px">Asthma</span>
  <span class="check" style="left:338px;top:348px"></span><span class="abs opt" style="left:353px;top:348px">Emphysema</span>
  <span class="check" style="left:423px;top:348px"></span><span class="abs opt" style="left:437px;top:348px">COPD</span>

  <span class="abs opt" style="left:21px;top:371px">LMP:</span>
  <div class="line" style="left:42px;top:378px;width:105px"></div>
  <span class="check" style="left:153px;top:371px"></span><span class="abs opt" style="left:167px;top:372px">BHCG</span>
  <span class="check" style="left:205px;top:371px"></span><span class="abs opt" style="left:218px;top:372px">Tubal ligation</span>
  <span class="check" style="left:283px;top:371px"></span><span class="abs opt" style="left:297px;top:371px">Post-menopause&gt;1 year</span>
  <span class="check" style="left:398px;top:371px"></span><span class="abs opt" style="left:409px;top:371px">Hysterectomy</span>

  <div class="abs divider"></div>
  <p class="abs notice">Please read the following instructions carefully. You might be rescheduled if any of the following instructions are not met.</p>

  <ul class="rules">
    <li style="left:40px;top:425px;width:170px"><svg class="tick" viewBox="0 0 10 10"><circle cx="5" cy="5" r="5" fill="#c0323b"/><path d="M2.6 5.2L4.3 6.8L7.4 3.4" stroke="#fff" stroke-width="1.3" fill="none"/></svg>AVOID caffeine containing products (coffee, tea, soda, chocolate, energy drinks, or some over the counter medications) for 4 hours prior to testing.</li>
    <li style="left:40px;top:456px;width:180px"><svg class="tick" viewBox="0 0 10 10"><circle cx="5" cy="5" r="5" fill="#c0323b"/><path d="M2.6 5.2L4.3 6.8L7.4 3.4" stroke="#fff" stroke-width="1.3" fill="none"/></svg>AVOID smoking for 4 hours prior to testing.</li>
    <li style="left:40px;top:471px;width:180px"><svg class="tick" viewBox="0 0 10 10"><circle cx="5" cy="5" r="5" fill="#c0323b"/><path d="M2.6 5.2L4.3 6.8L7.4 3.4" stroke="#fff" stroke-width="1.3" fill="none"/></svg>AVOID eating or drinking anything except water for 4 hours prior to testing.</li>
    <li style="left:40px;top:493px;width:180px"><svg class="tick" viewBox="0 0 10 10"><circle cx="5" cy="5" r="5" fill="#c0323b"/><path d="M2.6 5.2L4.3 6.8L7.4 3.4" stroke="#fff" stroke-width="1.3" fill="none"/></svg>Arrive 15 minutes early for your appointment time.</li>
    <li style="left:258px;top:425px;width:180px"><svg class="tick" viewBox="0 0 10 10"><circle cx="5" cy="5" r="5" fill="#c0323b"/><path d="M2.6 5.2L4.3 6.8L7.4 3.4" stroke="#fff" stroke-width="1.3" fill="none"/></svg>Wear comfortable clothing. Remove any metal objects, such as jewelry or piercings. Women will be asked to remove bras containing metal underwire.</li>
    <li style="left:258px;top:456px;width:180px"><svg class="tick" viewBox="0 0 10 10"><circle cx="5" cy="5" r="5" fill="#c0323b"/><path d="M2.6 5.2L4.3 6.8L7.4 3.4" stroke="#fff" stroke-width="1.3" fill="none"/></svg>Inform your physician or the staff if you are claustrophobic or have a problem staying in restricted environments for any length of time.</li>
    <li style="left:258px;top:486px;width:180px"><svg class="tick" viewBox="0 0 10 10"><circle cx="5" cy="5" r="5" fill="#c0323b"/><path d="M2.6 5.2L4.3 6.8L7.4 3.4" stroke="#fff" stroke-width="1.3" fill="none"/></svg>Inform the physician or the staff if you are or think you might be pregnant.</li>
  </ul>

  <p class="abs ack">I hereby acknowledge that the instructions and procedures pertinent to this study were explained thoroughly, I had time to ask questions, and these questions were addressed satisfactorily.</p>

  <div class="sig" style="left:21px;top:533px"><div class="sig__head sig__head--red">Patient's Print Name</div></div>
  <div class="sig" style="left:159px;top:533px"><div class="sig__head sig__head--red">Patient's Signature</div></div>
  <div class="sig" style="left:21px;top:568px"><div class="sig__head sig__head--dark">Prescriber's Print Name</div></div>
  <div class="sig" style="left:159px;top:568px"><div class="sig__head sig__head--dark">Prescriber's Signature</div></div>

  <div class="abs referral">
    <div class="referral__head">Referring Physician Contact Information</div>
    <div class="referral__row">ORDER DATE:</div>
    <div class="referral__row">TEL NO.:</div>
    <div class="referral__row">FAX NO.:</div>
  </div>
</section>

</body>
</html>
```